Spiritual journeyer, astrologer, Reiki master, underground music lover needs business card design

Initially I need a business card design (and possibly a logo for my new website). I offer astrological and energetic inquiry and guidance to clients in support of their life's evolutionary path. I combine an eclectic mix of methods with a focus on the mind body connection. I am a spiritual journeyer, astrologer, Reiki Master, certified personal trainer, soon to be black belt in Taekwondo (karate), and researcher into the benefits of music/sound vibrational therapy. And underground music lover :) The attached drawing is just something I drew freehand, it is symbolic of many things important to me. I wanted the figure to clearly be female. Her arms are open to catch the sky, the name of my new business is Noraweaver, and Nora is my daughter's name. This was just an idea I had, I'm open to suggestions. The photo is me with the planets in the sky as they were at the moment I was born (some years ago-LOL)

I have picked a final design. Thank you everyone for your time and effort.

Target Market(s)

Worldwide, what I do can be done in person or anywhere in the world via Skype

Industry/Entity Type

Professional Service

Contact Information for Business Card

Simple, unusual image with my business name and contact info

Font styles to use
Sans Serif

Requirements
Must have
• My website very clean, simple. Somehow combine biz name of Noraweaver with female figure catching/holding the starry sky? See my poor drawing I attached.
Nice to have
• Something that conveys all the unique, unusual, eclectic skills and capacities I have
Should not have
• Frilly, fancy, stuffy

```html
<!DOCTYPE html>
<html lang="en">
<head>
<meta charset="utf-8">
<title>Noraweaver business card</title>
<link rel="stylesheet" href="https://fonts.googleapis.com/css2?family=Open+Sans:wght@400;600&display=swap">
<style>
  :root {
    --page-bg: #e9e5e1;
    --card-top: #2b3541;
    --card-bottom: #222a33;
    --gold: #f2a81c;
    --text-light: #f4f4f4;
    --ring: #c9ccd0;
  }
  * { margin: 0; padding: 0; box-sizing: border-box; }
  html, body {
    width: 1200px; height: 900px; overflow: hidden;
    background: var(--page-bg);
    font-family: "Open Sans", sans-serif;
  }
  .canvas { position: relative; width: 1200px; height: 900px; }
  .card {
    position: absolute;
    width: 556px; height: 342px;
    background: radial-gradient(ellipse at 55% 35%, var(--card-top), var(--card-bottom) 75%);
    box-shadow: 0 6px 18px rgba(0,0,0,0.25);
  }
  .card--front { left: 238px; top: 62px; }
  .card--back { left: 457px; top: 519px; }

  .mark-ring {
    border: 6px solid var(--ring);
    border-radius: 50%;
  }
  .card--front .mark-ring {
    position: absolute;
    left: 70px; top: 81px;
    width: 164px; height: 164px;
  }

  .brand-mark {
    position: absolute;
    left: 0; top: 81px; width: 100%;
    display: flex; flex-direction: column; align-items: center;
  }
  .brand-mark .mark-ring { width: 130px; height: 130px; }
  .brand-mark__name {
    color: var(--gold);
    font-weight: 600;
    font-size: 44px;
    line-height: 1.1;
    margin-top: 10px;
    white-space: nowrap;
  }

  .details { position: absolute; left: 302px; top: 90px; }
  .details__name { color: var(--gold); font-size: 20px; font-weight: 600; line-height: 1.2; }
  .details__role { color: var(--text-light); font-size: 14.5px; line-height: 23px; margin-top: 3px; }
  .contact { list-style: none; margin-top: 16px; }
  .contact__item {
    display: flex; align-items: center; gap: 10px;
    color: var(--text-light); font-size: 14.5px; line-height: 23.5px;
  }
  .contact__icon { width: 12px; height: 12px; fill: var(--gold); flex: none; }
</style>
</head>
<body>
<div class="canvas">
  <section class="card card--front">
    <div class="mark-ring"></div>
    <div class="details">
      <h1 class="details__name">Miriam Hale</h1>
      <p class="details__role">Astrological and Energetic<br>Guidance and Inquiry</p>
      <ul class="contact">
        <li class="contact__item">
          <svg class="contact__icon" viewBox="0 0 12 12" aria-hidden="true"><path d="M2.4 0.6 L4.2 2.8 L3.3 4.2 Q4.6 6.9 7.8 8.7 L9.2 7.8 L11.4 9.6 L10.2 11.4 Q5.6 11.2 2.4 7.8 Q0.2 5 0.6 1.8 Z"/></svg>
          555-210-347
        </li>
        <li class="contact__item">
          <svg class="contact__icon" viewBox="0 0 12 12" aria-hidden="true"><path d="M0.5 2.5 H11.5 V9.5 H0.5 Z M1.2 3 L6 6.6 L10.8 3" stroke="#26303b" stroke-width="0.9"/></svg>
          info@noraweaver.com
        </li>
        <li class="contact__item">
          <svg class="contact__icon" viewBox="0 0 12 12" aria-hidden="true"><circle cx="6" cy="6" r="5.5"/><path d="M3 3.5 Q5 4 4.5 6 Q6.5 7 6 9.5 M8 2.5 Q7.5 4 9.5 5" stroke="#26303b" stroke-width="1" fill="none"/></svg>
          www.noraweaver.com
        </li>
      </ul>
    </div>
  </section>

  <section class="card card--back">
    <div class="brand-mark">
      <div class="mark-ring"></div>
      <div class="brand-mark__name">Noraweaver</div>
    </div>
  </section>
</div>
</body>
</html>
```